Construction Business Card & Stationary
LorvenCraft Homes and Commercial
I need single sided standard sized Business Card [3.5" x 2"]
Whatever looks the best
Professional
Dale Ostrand
715 Wexcombe Street
Regina, SK, S7T 2K9
Ph: (306) 555-0142
Cell: (306) 555-0178
Fx: (306) 555-0143
dale@lorvencraft.example
www.lorvencraft.example
See my final selected logo design on Zentavio @
http://www.zentavio.example/contests/construction-logo-1
I am looking for a business card design and 8.5x11 stationary for letters and construction specifications.
Recent design winner on this site. Here is the jpg to get started.
Icon @ Top
Icon @ Left

```html
<!DOCTYPE html>
<html lang="en">
<head>
<meta charset="utf-8">
<title>LorvenCraft Homes and Commercial — Business Card</title>
<link href="https://fonts.googleapis.com/css2?family=Arimo:wght@400;700&display=swap" rel="stylesheet">
<style>
  :root {
    --card-bg: #ffffff;
    --ink: #2b2b2b;
    --ink-soft: #3a3a3a;
    --brand-green: #8dc63f;
  }
  * { margin: 0; padding: 0; box-sizing: border-box; }
  html, body {
    width: 1200px;
    height: 686px;
    overflow: hidden;
    background: var(--card-bg);
  }
  .card {
    position: relative;
    width: 1200px;
    height: 686px;
    background: var(--card-bg);
    font-family: "Arimo", Arial, sans-serif;
    color: var(--ink);
  }
  .brand {
    position: absolute;
    left: 94px;
    top: 100px;
    width: 420px;
    text-align: center;
  }
  .brand-square {
    display: block;
    width: 134px;
    height: 134px;
    margin: 0 auto 10px;
    background: var(--brand-green);
  }
  .brand-name,
  .brand-tagline {
    font-weight: 700;
    color: var(--ink);
    white-space: nowrap;
  }
  .brand-name {
    font-size: 50px;
    line-height: 52px;
    letter-spacing: 1px;
  }
  .brand-tagline {
    font-size: 19px;
    line-height: 24px;
    letter-spacing: 1.5px;
  }
  .person-name {
    position: absolute;
    left: 94px;
    top: 410px;
    font-size: 31px;
    font-weight: 400;
    color: var(--ink);
  }
  .website {
    position: absolute;
    left: 94px;
    top: 588px;
    font-size: 29px;
    font-weight: 700;
    color: var(--brand-green);
  }
  .contact {
    position: absolute;
    left: 737px;
    top: 374px;
    font-size: 26px;
    line-height: 33px;
    color: var(--ink-soft);
  }
  .address { margin-bottom: 18px; }
  .contact-row { display: flex; }
  .contact-label { width: 82px; }
  .contact-row.email .contact-label { width: auto; margin-right: 6px; }
</style>
</head>
<body>
  <main class="card">
    <div class="brand">
      <span class="brand-square"></span>
      <div class="brand-name">LORVENCRAFT</div>
      <div class="brand-tagline">HOMES AND COMMERCIAL</div>
    </div>

    <p class="person-name">Dale Ostrand</p>
    <p class="website">www.lorvencraft.example</p>

    <div class="contact">
      <div class="address">
        <div>715 Wexcombe Street</div>
        <div>Regina, SK, S7T 2K9</div>
      </div>
      <div class="contact-row"><span class="contact-label">Ph</span><span>: (306) 555-0142</span></div>
      <div class="contact-row"><span class="contact-label">Fax</span><span>: (306) 555-0143</span></div>
      <div class="contact-row"><span class="contact-label">Cell</span><span>: (306) 555-0178</span></div>
      <div class="contact-row email"><span class="contact-label">Email:</span><span>dale@lorvencraft.example</span></div>
    </div>
  </main>
</body>
</html>
```